Aircraft maintenance buisness card

I am an aircraft mechanic looking for a personal buisness card . I would like my name and a title of Aircraft Maintenance Manager . I would like a suttle picture of an aircraft and helicopter .

elegant and professional wtih my contact .

My name should be on the car and Aircraft Maintenance Manager under with my contact infor below .

i have attached some pictures but i am open to other pics and ideas . I would like a airliner or private jet and a helicopter in the picture . The Images should be suttle and not the main idea . I also uploaded a picture of a jet engine which is cool . Be creative and i will work with you to finalize something .
Updates

Project Deadline Extended
Reason: Looking for more variations . Very good so far but looiking for a bit more styles and i uploaded my logo that i purchased . Please use my logo and be creative with it . I like some variations of black card with maybe some pictures that i uploaded but i am open to ideas . Be creative and i will work with you .

Project Deadline Extended
Reason: Looking for more designs and variations . Not yet satisfied with the designs i have gotten .

Industry/Entity Type

Aviation

Contact Information for Business Card

Aircraft Maintenance Manager

Font styles to use
Serif

Colors

Designer to choose colors to be used in the design.

Requirements
Must have
• An aviation related Logo if possible incorporated in the card possibly
• My name
• Tiberio Malvade Furtunato
• 482 Pellow St.
• Kearny , NJ
• 08519
• Email: Lwskyfixtech@mailvora.com
Nice to have
• Suttle Backround of a Private Jet or Airliner and a Helicopter .

```html
<!DOCTYPE html>
<html lang="en">
<head>
<meta charset="utf-8">
<title>Aircraft Maintenance Manager – Business Card</title>
<link href="https://fonts.googleapis.com/css2?family=Source+Sans+3:wght@400;600;700&display=swap" rel="stylesheet">
<style>
  :root {
    --backdrop: #616161;
    --white: #ffffff;
    --sky-blue: #0b93cf;
    --stripe-blue: #2ea4d8;
    --navy: #0f2554;
    --rock-light: #8a8f96;
    --forest: #3f5a3a;
    --overlay-blue: #2e3f66;
  }
  html, body {
    margin: 0;
    padding: 0;
    width: 1120px;
    height: 1200px;
    overflow: hidden;
    background: var(--backdrop);
    font-family: "Source Sans 3", "Myriad Pro", Arial, sans-serif;
  }
  .card {
    position: absolute;
    overflow: hidden;
    background: var(--white);
  }
  .card--front { left: 236px; top: 122px; width: 715px; height: 427px; }
  .card--back  { left: 238px; top: 617px; width: 716px; height: 429px; }

  .photo { position: absolute; left: 0; top: 0; }
  .card--front .photo {
    width: 715px; height: 390px;
    background:
      radial-gradient(ellipse 40% 30% at 50% 45%, rgba(255,255,255,0.25), transparent 70%),
      linear-gradient(180deg, var(--rock-light) 0%, #6f757c 60%, var(--forest) 100%);
  }
  .card--back .photo {
    width: 716px; height: 406px;
    background:
      radial-gradient(ellipse 30% 25% at 48% 55%, rgba(180,190,215,0.35), transparent 70%),
      linear-gradient(180deg, #3d4c70 0%, var(--overlay-blue) 60%, #24344f 100%);
  }
  .shapes { position: absolute; left: 0; top: 0; }

  .front-name {
    position: absolute;
    left: 68px; top: 31px;
    margin: 0;
    color: var(--white);
    font-weight: 700;
    font-size: 18.5px;
    line-height: 22px;
    text-transform: uppercase;
    letter-spacing: -0.2px;
  }
  .front-title {
    position: absolute;
    right: 44px; top: 390px;
    height: 37px;
    line-height: 37px;
    color: var(--white);
    font-weight: 600;
    font-size: 17.5px;
  }

  .brand {
    position: absolute;
    left: 490px; top: 28px;
    display: flex;
    align-items: center;
    gap: 8px;
  }
  .brand-square {
    width: 18px; height: 18px;
    background: var(--navy);
  }
  .brand-name {
    color: var(--navy);
    font-weight: 700;
    font-size: 24px;
    line-height: 28px;
  }

  .back-name {
    position: absolute;
    left: 24px; top: 112px;
    margin: 0;
    color: var(--white);
    font-weight: 600;
    font-size: 23.5px;
    line-height: 29px;
    text-transform: uppercase;
    letter-spacing: -0.3px;
  }
  .contact-list {
    position: absolute;
    left: 23px; top: 186px;
    margin: 0; padding: 0;
    list-style: none;
  }
  .contact-item {
    position: relative;
    padding-left: 42px;
    color: var(--white);
    font-weight: 600;
    font-size: 18.5px;
    line-height: 23px;
  }
  .contact-item--email { font-weight: 700; }
  .contact-item--phone { font-weight: 700; margin-top: 21px; }
  .contact-item--address { margin-top: 16px; }
  .contact-icon {
    position: absolute;
    left: 0; top: -4px;
    width: 30px; height: 30px;
  }
</style>
</head>
<body>

<section class="card card--front">
  <div class="photo" role="img" aria-label="Blue and white helicopter flying in front of a grey rock cliff"></div>
  <svg class="shapes" width="715" height="427" viewBox="0 0 715 427">
    <rect x="0" y="390" width="715" height="37" fill="var(--white)"/>
    <polygon points="351,390 715,390 715,427 313,427" fill="var(--sky-blue)"/>
  </svg>
  <h1 class="front-name">Tiberio Malvade<br>Furtunato</h1>
  <div class="front-title">Aircraft Maintenance Manager</div>
</section>

<section class="card card--back">
  <div class="photo" role="img" aria-label="Blue-tinted helicopter flying past a rock cliff"></div>
  <svg class="shapes" width="716" height="429" viewBox="0 0 716 429">
    <polygon points="331,0 716,0 716,406 601,406" fill="var(--stripe-blue)"/>
    <polygon points="372,0 716,0 716,406 603,406" fill="var(--white)"/>
    <rect x="0" y="406" width="716" height="23" fill="var(--sky-blue)"/>
  </svg>

  <div class="brand">
    <span class="brand-square"></span>
    <span class="brand-name">HALVERN AERO</span>
  </div>

  <h2 class="back-name">Tiberio Malvade<br>Furtunato</h2>

  <ul class="contact-list">
    <li class="contact-item contact-item--email">
      <svg class="contact-icon" viewBox="0 0 30 30" aria-hidden="true">
        <circle cx="15" cy="15" r="15" fill="var(--white)"/>
        <rect x="8" y="10" width="14" height="10" rx="1" fill="var(--overlay-blue)"/>
        <polyline points="8.5,10.5 15,16 21.5,10.5" fill="none" stroke="var(--white)" stroke-width="1.4"/>
      </svg>
      lwskyfixtech@mailvora.com
    </li>
    <li class="contact-item contact-item--phone">
      <svg class="contact-icon" viewBox="0 0 30 30" aria-hidden="true">
        <circle cx="15" cy="15" r="15" fill="var(--white)"/>
        <path d="M10.5 8.5 L13 8 L14.3 11.6 L12.6 13 Q14 16 17 17.4 L18.4 15.7 L22 17 L21.5 19.5 Q20.5 21.5 18 21 Q11.5 19 9 12 Q8.5 9.5 10.5 8.5 Z" fill="var(--overlay-blue)"/>
      </svg>
      08519
    </li>
    <li class="contact-item contact-item--address">
      <svg class="contact-icon" viewBox="0 0 30 30" aria-hidden="true">
        <circle cx="15" cy="15" r="15" fill="var(--white)"/>
        <path d="M15 7 C11.7 7 9.5 9.4 9.5 12.4 C9.5 16.3 15 23 15 23 C15 23 20.5 16.3 20.5 12.4 C20.5 9.4 18.3 7 15 7 Z" fill="var(--overlay-blue)"/>
        <circle cx="15" cy="12.5" r="2.2" fill="var(--white)"/>
      </svg>
      482 Pellow St.<br>Halvern, OH
    </li>
  </ul>
</section>

</body>
</html>
```